Cosmetic Clinic Looking For Sign Designs

We are looking for sign design ideas for the front of our building and a lawn sign for our cosmetic injection salon.
I have uploaded the front of our building for a mock up and size, lawn posts with size and a sign that uses the same dimensions.
We would like both signs to be black for the background.

Target Market(s)

Ages 18-75

Industry/Entity Type

Beauty

Requirements
Must have
• Services we offer:
• Cosmetic Injections
• Airbrush Spray Tanning
• Eyelash Growth Serum
• Skin Care Products & More
• Everything must be on a black background
• The lawn sign must have the address: 394 Fenwick and the building sign should have the phone number.
Should not have
• Nothing can light up (no LED)
• Both signs do not need the full address. Just 394 Fenwick and the phone number

```html
<!DOCTYPE html>
<html lang="en">
<head>
<meta charset="utf-8">
<title>Bright Hour Studio – Lawn Sign</title>
<link rel="stylesheet" href="https://fonts.googleapis.com/css2?family=Libre+Baskerville&display=swap">
<style>
  :root {
    --canvas-bg: #e9e9ea;
    --sign-black: #000000;
    --divider-violet: #7b78c4;
    --skin-light: #e8c2ad;
    --skin-mid: #c99580;
    --skin-shadow: #6e4a3e;
    --brand-teal: #1fa3b8;
    --service-white: #f4f4f4;
  }
  html, body {
    margin: 0;
    padding: 0;
    width: 900px;
    height: 1200px;
    overflow: hidden;
    background: var(--canvas-bg);
  }
  .canvas {
    position: relative;
    width: 900px;
    height: 1200px;
  }
  .lawn-sign {
    position: absolute;
    left: 70px;
    top: 192px;
    width: 760px;
    height: 815px;
    background: var(--sign-black);
    overflow: hidden;
    font-family: "Libre Baskerville", "Times New Roman", serif;
  }
  .sign-art {
    position: absolute;
    inset: 0;
    width: 760px;
    height: 815px;
  }
  .brand-name {
    position: absolute;
    left: 290px;
    width: 360px;
    top: 206px;
    margin: 0;
    text-align: center;
    font-size: 29px;
    font-weight: 400;
    letter-spacing: 1px;
    line-height: 1.2;
    color: var(--brand-teal);
  }
  .service-list {
    list-style: none;
    margin: 0;
    padding: 0;
  }
  .service {
    position: absolute;
    color: var(--service-white);
    font-size: 23px;
    letter-spacing: 2.4px;
    line-height: 1;
    white-space: nowrap;
  }
  .service--injections { left: 310px; top: 336px; }
  .service--tanning    { left: 324px; top: 391px; }
  .service--serum      { left: 336px; top: 446px; }
  .service--skincare   { left: 348px; top: 501px; }
  .address {
    position: absolute;
    left: 420px;
    top: 768px;
    margin: 0;
    display: flex;
    align-items: center;
    gap: 8px;
    color: var(--service-white);
    font-size: 21px;
    letter-spacing: 1.5px;
    line-height: 1;
  }
  .address-pin {
    width: 18px;
    height: 24px;
  }
</style>
</head>
<body>
<main class="canvas">
  <section class="lawn-sign">
    <svg class="sign-art" viewBox="0 0 760 815">
      <defs>
        <linearGradient id="portraitTone" x1="0" y1="0" x2="1" y2="1">
          <stop offset="0" stop-color="var(--skin-light)"/>
          <stop offset="0.55" stop-color="var(--skin-mid)"/>
          <stop offset="1" stop-color="var(--skin-shadow)"/>
        </linearGradient>
      </defs>
      <polygon class="portrait-panel" points="0,0 213,0 403,815 0,815" fill="url(#portraitTone)"
        role="img" aria-label="Close-up beauty photograph of a model's face with smoky eye makeup and teal lipstick"/>
      <line class="panel-divider" x1="213" y1="0" x2="403" y2="815" stroke="var(--divider-violet)" stroke-width="6"/>
    </svg>

    <h1 class="brand-name">Bright Hour Studio</h1>

    <ul class="service-list">
      <li class="service service--injections">Cosmetic Injections</li>
      <li class="service service--tanning">Airbrush Spray Tanning</li>
      <li class="service service--serum">Eyelash Growth Serum</li>
      <li class="service service--skincare">Skin Care Products &amp; More</li>
    </ul>

    <p class="address">
      <svg class="address-pin" viewBox="0 0 18 24" aria-hidden="true">
        <path d="M9 1C4.6 1 1.5 4.3 1.5 8.4 1.5 13.8 9 23 9 23s7.5-9.2 7.5-14.6C16.5 4.3 13.4 1 9 1z" fill="none" stroke="var(--divider-violet)" stroke-width="2.4"/>
        <circle cx="9" cy="8.6" r="2.6" fill="var(--divider-violet)"/>
      </svg>
      <span class="address-text">394 Fenwick</span>
    </p>
  </section>
</main>
</body>
</html>
```